Inviting A6 Flyer for Church membership

We need an A6 size flyer for the church. We are looking for something fresh, inviting and impactful. Church new logo and current flyer design attached.
Back text as follows:
We would love to have you join us as our SPECIAL GUEST this Sunday at 10am.
You can find us at Harvest Lantern Family Church, 17-19 Marlow Crest Road
(Behind Brivo), Thornbury Meadow Village,QX4 7LB
For more information or for a chat, please call us on 07700 900418 / 07700 900752 or email church@hlfcuk-mail.test
Target Market(s)
Church
Industry/Entity Type
Church
Colors
Designer to choose colors to be used in the design.
Requirements
Must have
- fresh, inviting and impactful.
- Chruch logo (attached)
Should not have
- Too much going on

```html
<!DOCTYPE html>
<html lang="en">
<head>
<meta charset="utf-8">
<title>Be Our Guest – Harvest Lantern Family Church Flyer</title>
<link href="https://fonts.googleapis.com/css2?family=Oswald:wght@500&family=Questrial&family=Kaushan+Script&display=swap" rel="stylesheet">
<style>
  :root {
    --board: #7a7a7a;
    --white: #ffffff;
    --red: #a31f1a;
    --ink: #333333;
    --script: #2e2e2e;
    --logo-blue: #2f6fb3;
  }
  * { margin: 0; padding: 0; box-sizing: border-box; }
  html, body { width: 1200px; height: 1200px; overflow: hidden; background: var(--board); }
  body { position: relative; font-family: "Questrial", sans-serif; color: var(--ink); }

  .flyer {
    position: absolute; left: 214px; width: 772px; height: 556px; overflow: hidden;
    box-shadow: 0 3px 8px rgba(0,0,0,.35);
  }
  .flyer--front { top: 30px; }
  .flyer--back { top: 619px; }

  .landscape { position: absolute; inset: 0; width: 100%; height: 100%; }

  .ring { position: absolute; border: 1px solid rgba(255,255,255,.8); border-radius: 50%; }
  .disc { position: absolute; background: var(--white); border-radius: 50%; }

  .headline {
    position: absolute; left: 12px; width: 772px; top: 136px; text-align: center;
    font-family: "Oswald", sans-serif; font-weight: 500; font-size: 72px; line-height: 1;
    color: var(--red); letter-spacing: -1px;
  }
  .headline-script {
    position: absolute; left: 0; width: 800px; top: 168px; text-align: center;
    font-family: "Kaushan Script", cursive; font-size: 200px; line-height: 1;
    color: var(--script);
  }

  .ministry-mark {
    position: absolute; text-align: center; width: 260px;
    display: flex; flex-direction: column; align-items: center; gap: 6px;
  }
  .ministry-mark__dot { width: 46px; height: 46px; border-radius: 50%; background: var(--logo-blue); }
  .ministry-mark__name { font-size: 13px; color: var(--red); letter-spacing: .5px; text-transform: uppercase; }

  .invite {
    position: absolute; left: 76px; width: 600px; top: 92px; text-align: center;
    font-size: 18px; line-height: 23px;
  }
  .invite__lead { margin-bottom: 6px; }
  .invite__special {
    font-family: "Oswald", sans-serif; font-weight: 500; font-size: 32px; line-height: 38px;
    letter-spacing: -.5px;
  }
  .invite__special .small { font-size: 22px; }
  .invite__special .accent { color: var(--red); }
  .divider { width: 6px; height: 6px; border-radius: 50%; background: var(--ink); margin: 18px auto 22px; }
  .address { color: var(--red); }
</style>
</head>
<body>

  <section class="flyer flyer--front">
    <svg class="landscape" viewBox="0 0 772 556" preserveAspectRatio="none" role="img" aria-label="Photograph of sunlit mountain ridges with golden grass under a purple sky">
      <defs>
        <linearGradient id="sky-front" x1="0" y1="0" x2="1" y2="1">
          <stop offset="0" stop-color="#f6c66a"/>
          <stop offset="0.35" stop-color="#c98a6a"/>
          <stop offset="0.7" stop-color="#5c5486"/>
          <stop offset="1" stop-color="#4a4a78"/>
        </linearGradient>
        <linearGradient id="ground-front" x1="0" y1="0" x2="0" y2="1">
          <stop offset="0" stop-color="rgba(176,120,70,0)"/>
          <stop offset="1" stop-color="#b88a40"/>
        </linearGradient>
        <radialGradient id="sun-front" cx="0.1" cy="0.1" r="0.45">
          <stop offset="0" stop-color="#fff6d0"/>
          <stop offset="1" stop-color="rgba(255,230,160,0)"/>
        </radialGradient>
      </defs>
      <rect width="772" height="556" fill="url(#sky-front)"/>
      <rect y="200" width="772" height="356" fill="url(#ground-front)"/>
      <rect width="772" height="556" fill="url(#sun-front)"/>
    </svg>
    <div class="ring" style="left:136px; top:24px; width:520px; height:520px;"></div>
    <div class="disc" style="left:148px; top:40px; width:488px; height:488px;"></div>

    <h1 class="headline">BE OUR</h1>
    <p class="headline-script">Guest</p>

    <div class="ministry-mark" style="left:262px; top:408px;">
      <span class="ministry-mark__dot"></span>
      <span class="ministry-mark__name">Harvest Lantern Ministries</span>
    </div>
  </section>

  <section class="flyer flyer--back">
    <svg class="landscape" viewBox="0 0 772 556" preserveAspectRatio="none" role="img" aria-label="Photograph of sunlit mountain ridges with golden grass under a purple sky">
      <defs>
        <linearGradient id="sky-back" x1="0" y1="0" x2="1" y2="1">
          <stop offset="0" stop-color="#f6c66a"/>
          <stop offset="0.35" stop-color="#c98a6a"/>
          <stop offset="0.7" stop-color="#5c5486"/>
          <stop offset="1" stop-color="#4a4a78"/>
        </linearGradient>
        <linearGradient id="ground-back" x1="0" y1="0" x2="0" y2="1">
          <stop offset="0" stop-color="rgba(176,120,70,0)"/>
          <stop offset="1" stop-color="#b88a40"/>
        </linearGradient>
        <radialGradient id="sun-back" cx="0.12" cy="0.12" r="0.45">
          <stop offset="0" stop-color="#fff6d0"/>
          <stop offset="1" stop-color="rgba(255,230,160,0)"/>
        </radialGradient>
      </defs>
      <rect width="772" height="556" fill="url(#sky-back)"/>
      <rect y="200" width="772" height="356" fill="url(#ground-back)"/>
      <rect width="772" height="556" fill="url(#sun-back)"/>
    </svg>
    <div class="ring" style="left:102px; top:8px; width:548px; height:548px;"></div>
    <div class="disc" style="left:118px; top:24px; width:516px; height:516px;"></div>

    <div class="invite">
      <p class="invite__lead">We would love to<br>have you join us as our</p>
      <p class="invite__special">SPECIAL GUEST <span class="small">this</span> <span class="accent">Sunday at 10am</span>.</p>
      <div class="divider"></div>
      <p>You can find us at</p>
      <p class="address">Harvest Lantern Family Church, 17-19 Marlow Crest Road<br>(Behind Brivo), Thornbury Meadow Village, QX4 7LB</p>
      <div class="divider"></div>
      <p>For more information or for a chat, please call us on<br>07700 900418 / 07700 900752 or<br>email: church@hlfcuk-mail.test</p>
    </div>

    <div class="ministry-mark" style="left:246px; top:440px;">
      <span class="ministry-mark__dot" style="width:40px; height:40px;"></span>
      <span class="ministry-mark__name" style="font-size:12px;">Harvest Lantern Ministries</span>
    </div>
  </section>

</body>
</html>
```